Business card for a new innovative and professional lawn care business

We need a business card design for a new lawn care business in Halifax NS Canada. We offer lawn services in Halifax & Bedford. Our services offered include lawn care, garden services, and property maintenance. We take pride in our work and are experienced at what we do. I would like to see a design that is double sided. On the backside I would like the something simple (maybe my logo preferably on blackround (linked below) with website link, Facebook page or something). The front I want to include contact info:
Darren Maple
phone 902-555-0148
email - darrensyardworks.ca
facebook - Facebook.com/darrensyardworks
Instagram maybe ? - instagram.com/darrenyardworks
Serving Halifax and Bedford for 5 years?
I don't want it to have too much information as I will be passing them out in aim to visit website, or call !
We do want it to include lawn care, garden services and property maintenance.
Basic, catchy, and modern looking !
Logo attached below !

Target Market(s)

Passing business cards to everyone I meet or interact with.

Industry/Entity Type

Lawn Care

Contact Information for Business Card

Double sided with some basic information, with catchy colours and easy to look at.

Font styles to use
Sans Serif

Requirements
Must have
• Must be double sided and have :
• Name, Phone, Email, FB, Website, and 3 main services offered - lawn care, property maintenance, garden services
Nice to have
• Would be nice to have instagram link if it goes well on there
Should not have
• Don't want too much writing or images that are distracting

```html
<!DOCTYPE html>
<html lang="en">
<head>
<meta charset="utf-8">
<title>Darren's Yardworks – Business Card</title>
<link href="https://fonts.googleapis.com/css2?family=Barlow+Semi+Condensed:wght@400;600;700&display=swap" rel="stylesheet">
<style>
  :root {
    --bg: #e4e2de;
    --card: #ffffff;
    --green-light: #8cc63f;
    --green-dark: #1f7a2c;
    --shadow: rgba(0, 0, 0, 0.18);
  }
  * { margin: 0; padding: 0; box-sizing: border-box; }
  html, body {
    width: 1200px;
    height: 843px;
    overflow: hidden;
    background: var(--bg);
    font-family: "Barlow Semi Condensed", sans-serif;
  }
  .canvas {
    width: 1200px;
    height: 843px;
    display: flex;
    align-items: center;
    justify-content: center;
    gap: 60px;
  }
  .card {
    width: 520px;
    height: 297px;
    padding: 0 30px;
    background: var(--card);
    box-shadow: 0 6px 18px var(--shadow);
    display: flex;
    flex-direction: column;
    align-items: center;
    justify-content: center;
  }

  /* Contact side */
  .holder-name {
    color: var(--green-light);
    font-weight: 400;
    font-size: 26px;
    letter-spacing: 0.28em;
    text-transform: uppercase;
    margin-bottom: 30px;
  }
  .contact-list { list-style: none; }
  .contact-item {
    display: flex;
    align-items: center;
    gap: 8px;
    color: var(--green-dark);
    font-weight: 600;
    font-size: 15px;
    letter-spacing: 0.22em;
    text-transform: uppercase;
    line-height: 24px;
  }
  .contact-item:first-child { font-size: 17px; }
  .contact-icon { width: 12px; height: 12px; flex: none; }
  .contact-icon * { fill: var(--green-light); }

  /* Brand side */
  .brand {
    display: flex;
    align-items: center;
    gap: 12px;
  }
  .brand-mark {
    width: 24px;
    height: 24px;
    border-radius: 50%;
    background: var(--green-light);
    flex: none;
  }
  .brand-name {
    color: var(--green-dark);
    font-weight: 700;
    font-size: 38px;
    letter-spacing: 0.04em;
    text-transform: uppercase;
    line-height: 1;
    white-space: nowrap;
  }
  .brand-url {
    margin-top: 18px;
    color: var(--green-dark);
    font-weight: 600;
    font-size: 15px;
    letter-spacing: 0.3em;
    text-transform: uppercase;
  }
  .service-list {
    list-style: none;
    display: flex;
    gap: 18px;
    margin-top: 16px;
  }
  .service-item {
    color: var(--green-light);
    font-weight: 600;
    font-size: 12px;
    letter-spacing: 0.16em;
    text-transform: uppercase;
    white-space: nowrap;
  }
</style>
</head>
<body>
<main class="canvas">
  <section class="card card-contact" aria-label="Card front">
    <h1 class="holder-name">Darren Maple</h1>
    <ul class="contact-list">
      <li class="contact-item">
        <svg class="contact-icon" viewBox="0 0 12 12" aria-hidden="true"><path d="M2.4 1h2l1 2.6-1.3 1a6.5 6.5 0 0 0 3.3 3.3l1-1.3 2.6 1v2c0 .6-.5 1-1.1 1A9.5 9.5 0 0 1 1.4 2.1C1.4 1.5 1.8 1 2.4 1z"/></svg>
        902-555-0148
      </li>
      <li class="contact-item">
        <svg class="contact-icon" viewBox="0 0 12 12" aria-hidden="true"><circle cx="6" cy="6" r="5.5"/></svg>
        darrensyardworks.ca
      </li>
      <li class="contact-item">
        <svg class="contact-icon" viewBox="0 0 12 12" aria-hidden="true"><rect x="0.5" y="0.5" width="11" height="11" rx="2"/></svg>
        /darrensyardworks
      </li>
      <li class="contact-item">
        <svg class="contact-icon" viewBox="0 0 12 12" aria-hidden="true"><rect x="0.5" y="0.5" width="11" height="11" rx="2"/></svg>
        /darrenyardworks
      </li>
    </ul>
  </section>

  <section class="card card-brand" aria-label="Card back">
    <div class="brand">
      <span class="brand-mark" aria-hidden="true"></span>
      <span class="brand-name">Darren's Yardworks</span>
    </div>
    <p class="brand-url">darrensyardworks.ca</p>
    <ul class="service-list">
      <li class="service-item">Lawn Care</li>
      <li class="service-item">Garden Services</li>
      <li class="service-item">Property Maintenance</li>
    </ul>
  </section>
</main>
</body>
</html>
```